Harbourline Sonography Academy (Kestrel Institute of Clinical Scanning) needs an additional web design f

Don't require a redesign of our existing website, I need an additional web design to compliment and feed into our existing web page (kics.edu.au) but establish excellent zintro rankings in it's own right. Web page is to appeal to a specific target market in the allied health industry who wish to learn how to do ultrasound on patients. New website is www. frontlinescanskills.com.au. Our educational institution delivers hands on workshops and seminars on ANYTHING involved with EMERGENCY Ultrasound - intro, advanced, doctors, nurses, etc. Our competitors in this field www.bedsidewavelabs.com.au and www.qpo.edu.au. Looking for a design that will capture the target audience and deliver the message that the courses are delivered by one of the best faculties in Australia. SEO strategies are paramount in that we don't wish to be penalised by Zintro by running a feeder site. Courses are delivered in Sydney and are accredited by an organisation called BRAV.com.au. The courses are listed under 2 qualifications on BRAV website - DLTX and KMRTE. Registrants of our courses are striving to achieve either DLTX - Certificate in Bedside Operator Sonography http://www.brav.com.au/newsite/Files/Documents/Education/DLTX/DLTX_Course_Brochure.pdf OR KMRTE - Certificate in Support Staff Operated Echography http://www.brav.com.au/newsite/Files/Documents/Education/KMRTE/KMRTE_Course_Brochure.pdf.
Website to be lumofon, smartphone and tablet compatible.

Target Market(s)

Emergency Physicians and Emergency nurses/doctors.

Industry/Entity Type

School

Coding

Coded - Design and coding required

Number of Pages Required

2 page

Other font styles liked:
• See website http://www.oakpointdental.com.au/

Colors
86cae6
ec1f27

Requirements
Must have
• Overall professional feel but easy to read and informative.
• Links to our normal website pages www.kics.edu.au
• Ability to rank high.
• Copy of material we deliver here http://www.kics.edu.au/emergency-ultrasound-course-1-3-days/ Click through on relevant dates for more information.
Nice to have
• I like this website - font, feel, layout etc.
• http://www.oakpointdental.com.au/
Should not have
• Information that will lower our zintro rankings knowing it is linked to www.kics.edu.au

```html
<!DOCTYPE html>
<html lang="en">
<head>
<meta charset="utf-8">
<title>Frontline Scan Skills</title>
<link href="https://fonts.googleapis.com/css2?family=Roboto:wght@400;500;700&family=Roboto+Condensed:wght@400;700&display=swap" rel="stylesheet">
<style>
:root{
  --blue:#86cae6;
  --blue-deep:#1f86b0;
  --nav-active:#1b82a8;
  --red:#ec1f27;
  --ink:#222;
  --muted:#555;
  --soft-bg:#f2f2f2;
  --rule:#cfcfcf;
  --footer:#231f20;
  --white:#fff;
}
*{margin:0;padding:0;box-sizing:border-box}
html,body{width:682px;height:1200px;overflow:hidden;background:var(--white)}
body{position:relative;font-family:'Roboto',sans-serif;color:var(--ink)}
.abs{position:absolute}

/* header */
.site-header{left:0;top:0;width:682px;height:71px;background:var(--white)}
.brand{left:86px;top:13px;display:flex;align-items:center;gap:8px}
.brand-dot{width:38px;height:38px;border-radius:50%;background:var(--blue-deep)}
.brand-name{font-family:'Roboto Condensed',sans-serif;font-size:15px;line-height:18px;color:var(--blue-deep);width:130px}
.follow{left:424px;top:11px;display:flex;align-items:center;gap:4px;font-size:7px;color:#777}
.follow .dot{width:10px;height:10px;border-radius:50%;background:var(--blue)}
.search{left:516px;top:8px;width:80px;height:18px;border:1px solid #ccc;font-size:7px;color:#777;padding:4px 0 0 14px}
.search svg{position:absolute;left:4px;top:4px}
.main-nav{left:298px;top:45px;display:flex;font-size:7.5px;color:var(--ink)}
.main-nav a{color:inherit;text-decoration:none;padding:0 8px;height:17px;line-height:17px}
.main-nav a.active{background:var(--nav-active);color:var(--white);padding:0 9px;margin-right:2px}

/* hero */
.hero{left:0;top:71px;width:682px;height:299px;background:linear-gradient(100deg,#e9e4e0 0%,#2f5f8f 35%,#d8dcd8 55%,#bfc3c0 100%)}
.hero-arrow{top:215px;width:31px;height:31px;border-radius:50%;background:rgba(60,60,60,.6)}

/* kmrte */
.intro-band{left:0;top:370px;width:682px;height:200px;background:var(--soft-bg)}
.center{width:682px;text-align:center;left:0}
.intro-title{top:379px;font-family:'Roboto Condensed',sans-serif;font-weight:700;font-size:13px;color:var(--red)}
.intro-text{top:395px;font-size:8.3px;line-height:12px;color:#444}
.btn-outline{left:311px;top:423px;width:60px;height:21px;border:1px solid var(--blue);color:var(--blue);font-family:'Roboto Condensed',sans-serif;font-weight:700;font-size:8px;text-align:center;line-height:19px}
.thumbs{left:86px;top:454px;display:flex;gap:1px}
.thumbs div{width:169px;height:104px}

/* course */
.course-title{top:585px;font-family:'Roboto Condensed',sans-serif;font-weight:700;font-size:9.5px;color:var(--blue-deep)}
.course-sub{top:598px;font-size:6.5px;color:#333}
.rule{height:1px;background:var(--rule)}
.col-head{font-family:'Roboto Condensed',sans-serif;font-weight:700;font-size:7.5px;color:var(--red)}
.ticks{list-style:none;font-size:6.5px;color:#222}
.ticks li{position:relative;padding-left:8px;height:14.8px;line-height:10px}
.ticks li::before{content:"";position:absolute;left:1px;top:2.5px;border-left:3px solid #222;border-top:2.5px solid transparent;border-bottom:2.5px solid transparent}
.note{font-size:6.5px;line-height:10.5px;color:#222}
.note b{font-weight:500}
.photo-frame{left:422px;top:628px;width:175px;height:182px;background:#e9e9e9;box-shadow:0 3px 5px rgba(0,0,0,.25);padding:3px}
.photo-frame div{width:169px;height:85px;margin-bottom:2px}

.book{top:833px;width:251px;height:81px;background:var(--blue);padding:10px 13px;color:var(--white)}
.book h3{font-family:'Roboto Condensed',sans-serif;font-weight:700;font-size:8.5px;margin-bottom:5px}
.book li{list-style:none;font-size:6.5px;color:#1b2a33;height:15.5px;padding-left:10px;position:relative}
.book li::before{content:"";position:absolute;left:0;top:2px;width:3.5px;height:3.5px;border-radius:50%;background:var(--red)}

/* dltx */
.dltx{left:0;top:929px;width:682px;height:193px;background:linear-gradient(90deg,#6f7479 0%,#55595d 50%,#7a7f83 100%)}
.dltx-title{top:951px;font-family:'Roboto Condensed',sans-serif;font-weight:700;font-size:22px;color:var(--white)}
.dltx-lead{top:984px;font-size:8.3px;color:var(--white)}
.dltx-text{top:1000px;font-size:8px;line-height:13.5px;color:#d5d5d5}
.dltx-mail{top:1051px;font-family:'Roboto Condensed',sans-serif;font-weight:700;font-size:7.5px;color:var(--white)}
.btn-light{left:311px;top:1078px;width:60px;height:21px;border:1px solid var(--white);color:var(--white);font-family:'Roboto Condensed',sans-serif;font-weight:700;font-size:8px;text-align:center;line-height:19px}

/* footer */
.site-footer{left:0;top:1122px;width:682px;height:78px;background:var(--footer)}
.foot-follow{left:300px;top:1134px;display:flex;align-items:center;gap:4px;font-family:'Roboto Condensed',sans-serif;font-weight:700;font-size:7px;color:var(--white)}
.foot-follow .dot{width:11px;height:11px;border-radius:50%;background:#666}
.foot-links{top:1169px;font-size:6px;color:#aaa;word-spacing:1px}
.foot-copy{top:1180px;font-size:6px;color:#aaa}
</style>
</head>
<body>

<header class="site-header abs">
  <div class="brand abs"><span class="brand-dot"></span><span class="brand-name">Frontline Scan Skills</span></div>
  <div class="follow abs">FOLLOW <span class="dot"></span><span class="dot"></span><span class="dot"></span></div>
  <div class="search abs"><svg width="7" height="7" viewBox="0 0 10 10"><circle cx="4" cy="4" r="3" fill="none" stroke="#777" stroke-width="1.3"/><line x1="6.2" y1="6.2" x2="9" y2="9" stroke="#777" stroke-width="1.3"/></svg>SEARCH</div>
  <nav class="main-nav abs">
    <a class="active" href="#">HOME</a><a href="#">ABOUT US</a><a href="#">SEMINARS</a><a href="#">OUR COURSES</a><a href="#">BLOG</a><a href="#">CONTACT US</a>
  </nav>
</header>

<section class="hero abs" role="img" aria-label="Smiling nurse in blue scrubs beside an ultrasound monitor in a clinic"></section>
<svg class="hero-arrow abs" style="left:71px" viewBox="0 0 31 31"><polyline points="18,8 11,15.5 18,23" fill="none" stroke="#fff" stroke-width="1.3"/></svg>
<svg class="hero-arrow abs" style="left:580px" viewBox="0 0 31 31"><polyline points="13,8 20,15.5 13,23" fill="none" stroke="#fff" stroke-width="1.3"/></svg>

<section class="intro-band abs"></section>
<h2 class="intro-title abs center">KMRTE</h2>
<p class="intro-text abs center">The KMRTE is a credential awarded by the BRAV Council to allied health practitioners who are not imaging specialists but who may use<br>ultrasound as a diagnostic tool at the point of care.</p>
<a class="btn-outline abs">READ MORE</a>
<div class="thumbs abs">
  <div role="img" aria-label="Ultrasound machine control panel" style="background:linear-gradient(135deg,#cfd6dc,#8ea2b6)"></div>
  <div role="img" aria-label="Gloved hand scanning an infant's head" style="background:linear-gradient(135deg,#8a8f94,#d8c8bc)"></div>
  <div role="img" aria-label="Interior of an ambulance" style="background:linear-gradient(135deg,#5f6366,#a9a59c)"></div>
</div>

<h2 class="course-title abs center">EMERGENCY ULTRASOUND COURSE</h2>
<p class="course-sub abs center">KESTREL INSTITUTE OF CLINICAL SCANNING AND SCANWELL VILLAGE</p>
<div class="rule abs" style="left:86px;top:613px;width:510px"></div>

<h3 class="col-head abs" style="left:86px;top:628px">FEATURES</h3>
<ul class="ticks abs" style="left:86px;top:645px">
  <li>Online Lectures – Prerequisite physics</li><li>Maximal hands on scanning time</li><li>Structured Reports</li><li>Opportunity for Logbook submission</li>
</ul>
<h3 class="col-head abs" style="left:259px;top:628px">DESIGNED AND DELIVERED BY</h3>
<ul class="ticks abs" style="left:259px;top:645px">
  <li>Emergency Physicians</li><li>Sonographers</li><li>Medical Educationalists</li>
</ul>

<div class="rule abs" style="left:86px;top:706px;width:312px"></div>
<p class="note abs" style="left:87px;top:715px;width:312px">This course has been accredited by EMCA and BRAV for AAA, E-FAST, Vascular Access, DVT and Basic Cardiac. Please see Scanwell Village for accreditation details.<br><b>Approved for RURAL GP GRANTS FOR EMERGENCY</b></p>
<div class="rule abs" style="left:86px;top:754px;width:312px"></div>
<p class="note abs" style="left:87px;top:764px"><b>EMERGENCY ULTRASOUND COURSE – 2 DAYS</b></p>
<ul class="ticks abs" style="left:88px;top:779px">
  <li>ULTRASOUND ESSENTIALS</li><li>ABDOMINAL AORTIC ANEURYSM (AAA)</li><li>E-FAST</li>
</ul>
<ul class="ticks abs" style="left:260px;top:779px">
  <li>VASCULAR ACCESS</li><li>FOREIGN BODIES</li><li>DVT</li>
</ul>

<div class="photo-frame abs">
  <div role="img" aria-label="Clinician performing an ultrasound scan on a patient" style="background:linear-gradient(135deg,#dfe3e6,#6e7f8c)"></div>
  <div role="img" aria-label="Hand holding an ultrasound probe in blue light" style="background:linear-gradient(135deg,#1f56b8,#cfe0ef)"></div>
</div>

<div class="book abs" style="left:86px">
  <h3>BOOK THIS SEMINAR</h3>
  <ul><li>29/01/2015 from 8:00 AM to 30/01/2015 3:00 PM</li><li>14/05/2015 from 8:00 AM to 15/05/2015 3:00 PM</li><li>03/09/2015 from 8:00 AM to 04/09/2015 3:00 PM</li></ul>
</div>
<div class="book abs" style="left:346px">
  <h3>BOOK THIS SEMINAR</h3>
  <ul><li>31/01/2015 from 8:00 AM to 31/01/2015 3:50 PM</li><li>16/05/2015 from 8:00 AM to 16/05/2015 3:50 PM</li><li>05/09/2015 from 8:00 AM to 05/09/2015 3:50 PM</li></ul>
</div>

<section class="dltx abs" role="img" aria-label="Doctor scanning a patient at the bedside, darkened background photo"></section>
<h2 class="dltx-title abs center">DLTX</h2>
<p class="dltx-lead abs center">The DLTX is available to medical practitioners who are practicing and registered with their national medical registration authority</p>
<p class="dltx-text abs center">The DLTX is a credential awarded by the BRAV Council to medical practitioners who are not imaging specialists but who may use<br>ultrasound as a diagnostic tool at the point of care. The DLTX represents a level of proficiency in image acquisition, optimisation<br>and ultrasound skills relevant to the specialty medical area.</p>
<p class="dltx-mail abs center">FOR ENQUIRES ABOUT THE DLTX EMAIL DLTX@BRAV.COM.AU</p>
<a class="btn-light abs">READ MORE</a>

<footer class="site-footer abs"></footer>
<div class="foot-follow abs">FOLLOW &nbsp;<span class="dot"></span><span class="dot"></span><span class="dot"></span></div>
<div class="rule abs" style="left:86px;top:1158px;width:510px;background:#3a3637"></div>
<p class="foot-links abs center">HOME | ABOUT US | SERVICES | OUR COURSES | BLOG | CONTACT US</p>
<p class="foot-copy abs center">COPYRIGHTS @ 2014 ALL RIGHTS RESERVED</p>

</body>
</html>
```